Meadowlark Behavioral Partners, LLC Needs Modern Business Card Design.

We provide behavioral health services from western Kansas to eastern Kansas. There is an abundance of competition for the services we provide with our main competitor being larger and having significantly more financial resources; however, the quality of services we provide is greater and we have started to catch the attention of the State of Kansas. We had a great logo designed by PixelGuild - this will be used to build upon our brand. The logo (attached) should be used in the card development. We want something unique, modern, but also a card design that clearly states our name, contact info, provides the name and unqiue location of each clinician, etc. Rounded edges, or a unique size, just something that makes our business card stand out from others. I have also uploaded each clinician's name and their unique location and phone number.

Our idea is to have one side be black with our logo. Then, on the other side have business cards for each individual. Plus, we want one card that is "generic" with no specific clinician's name listed so that we can give clients an appointment card when they leave. Some clinicians have two locations - we're open to design and background color, but we have started going with branding colors of black, the yellow in the logo files attached, and sometimes a gray. Our new office has been decorated using this theme.

Target Market(s)

individuals and families in need of behavioral health services; potential professional referral sources; existing referral sources

Industry/Entity Type

Business

Contact Information for Business Card

I attached a Word doc that provides clinician names, credentials and location information specific to each individual.

Font styles to use
Serif

Colors
000000
fbed22
dbdbdb
9d9d9d
c3c3c3

Requirements
Must have
• 1) use of the company logo that has been attached; 2) a template that provides us space to individualize business cards for all of our clinicians; 3) should stick to the colors we are branding with: black, yellow from the logo file, maybe a gray shade and we're open to a suggestion on a shade of white.
Nice to have
• Group discussion culminated in the thought that one side would be black with just our logo - no clinician names, etc. A unique design - rounded edges, unique size, some catchy lay-out would be nice.
Should not have
• Must not be too busy. Should look "clean." The project should stick to branding colors: black, yellow (from the logo file), maybe a gray and shade of white.

```html
<!DOCTYPE html>
<html lang="en">
<head>
<meta charset="utf-8">
<title>Meadowlark Behavioral Partners – Business &amp; Appointment Cards</title>
<link href="https://fonts.googleapis.com/css2?family=Open+Sans:wght@400;600;700&display=swap" rel="stylesheet">
<style>
  :root {
    --ink: #000000;
    --card-black: #0b0b0b;
    --brand-yellow: #f6c21a;
    --paper: #ffffff;
    --text-light: #e6e6e6;
    --text-dark: #1a1a1a;
    --rule: #333333;
    --backdrop: #dbdbdb;
  }
  * { box-sizing: border-box; margin: 0; padding: 0; }
  html, body { width: 1200px; height: 900px; overflow: hidden; }
  body {
    background: var(--backdrop);
    font-family: "Open Sans", Arial, sans-serif;
    position: relative;
  }
  .card {
    position: absolute;
    top: 300px;
    width: 525px;
    height: 300px;
    border-radius: 6px;
    box-shadow: 0 6px 18px rgba(0,0,0,0.18);
  }
  /* Business card – black side */
  .business-card {
    left: 55px;
    background: var(--card-black);
    color: var(--text-light);
  }
  .brand-lockup {
    position: absolute;
    left: 34px;
    bottom: 52px;
    display: flex;
    align-items: center;
    gap: 10px;
  }
  .brand-dot {
    width: 22px; height: 22px;
    border-radius: 50%;
    background: var(--brand-yellow);
    flex: none;
  }
  .brand-name {
    color: var(--brand-yellow);
    font-weight: 600;
    font-size: 15px;
    line-height: 1.25;
    letter-spacing: 0.04em;
    text-transform: uppercase;
  }
  .clinician {
    position: absolute;
    left: 300px;
    top: 36px;
    font-size: 12.5px;
    line-height: 1.5;
  }
  .clinician-name {
    color: var(--brand-yellow);
    font-weight: 700;
    font-size: 16px;
    line-height: 1.2;
  }
  .clinician-title { margin-bottom: 16px; }
  .location { margin-bottom: 14px; }
  .phone { display: flex; align-items: center; gap: 8px; }
  .phone svg { width: 11px; height: 11px; fill: var(--brand-yellow); }

  /* Appointment card – white side */
  .appointment-card {
    left: 620px;
    background: var(--paper);
    color: var(--text-dark);
    text-align: center;
  }
  .appointment-heading {
    margin-top: 34px;
    font-weight: 400;
    letter-spacing: 0.08em;
    text-transform: uppercase;
    line-height: 1.15;
  }
  .appointment-heading .line-main { font-size: 24px; display: block; }
  .appointment-heading .line-sub { font-size: 13px; display: block; }
  .appointment-form {
    width: 330px;
    margin: 26px auto 0;
    text-align: left;
    font-size: 12px;
  }
  .form-row { display: flex; align-items: flex-end; gap: 6px; margin-bottom: 10px; }
  .form-row .fill { flex: 1; border-bottom: 1px solid var(--rule); height: 14px; }
  .form-org { font-weight: 700; margin-bottom: 10px; }
  .tagline {
    margin-top: 20px;
    font-size: 17px;
    font-weight: 600;
  }
</style>
</head>
<body>

<section class="card business-card" aria-label="Clinician business card">
  <div class="brand-lockup">
    <span class="brand-dot"></span>
    <span class="brand-name">Meadowlark<br>Behavioral Partners, LLC</span>
  </div>
  <div class="clinician">
    <p class="clinician-name">Grant L. Holloway, LP</p>
    <p class="clinician-title">President</p>
    <div class="location">
      <p>418 N. Cedar Ave.</p>
      <p>Larkfield, Kansas 67203</p>
      <p class="phone"><svg viewBox="0 0 24 24" aria-hidden="true"><path d="M6.6 10.8a15.1 15.1 0 0 0 6.6 6.6l2.2-2.2a1 1 0 0 1 1-.25 11.4 11.4 0 0 0 3.6.57 1 1 0 0 1 1 1V20a1 1 0 0 1-1 1A17 17 0 0 1 3 4a1 1 0 0 1 1-1h3.5a1 1 0 0 1 1 1c0 1.250.2 2.450.57 3.6a1 1 0 0 1-.25 1z"/></svg>(316) 555-0142</p>
    </div>
    <div class="location">
      <p>207 E. Main St., Ste. 110</p>
      <p>Fairhaven, Kansas 66990</p>
      <p class="phone"><svg viewBox="0 0 24 24" aria-hidden="true"><path d="M6.6 10.8a15.1 15.1 0 0 0 6.6 6.6l2.2-2.2a1 1 0 0 1 1-.25 11.4 11.4 0 0 0 3.6.57 1 1 0 0 1 1 1V20a1 1 0 0 1-1 1A17 17 0 0 1 3 4a1 1 0 0 1 1-1h3.5a1 1 0 0 1 1 1c0 1.250.2 2.450.57 3.6a1 1 0 0 1-.25 1z"/></svg>(844) 555-0176</p>
    </div>
  </div>
</section>

<section class="card appointment-card" aria-label="Appointment card">
  <h1 class="appointment-heading">
    <span class="line-main">Meadowlark</span>
    <span class="line-sub">Behavioral Partners, LLC</span>
  </h1>
  <div class="appointment-form">
    <p class="form-org">Meadowlark Behavioral Partners, LLC</p>
    <div class="form-row"><span>Your next appointment with</span><span class="fill"></span></div>
    <div class="form-row"><span>Has been scheduled for</span><span class="fill"></span></div>
  </div>
  <p class="tagline">“Brighter days ahead.”</p>
</section>

</body>
</html>
```